Dental hygiene website

I would like to design to website that both dental professionals and the public can get information. I would also like a shopping cart as well. The name of the company is called Trevol. We have a product called the brightwave. Delia is the Ceo. Morgan is the CIO. Felipe is the COO. We are based in Parkland, Fl. The site should have a clean modern look that possibly has a natural/nature/ocean theme. We believe in an overall healthy lifestyle. We would like links to twitter/instagram/facebook. i would like to make additions to my shopping cart when we bring on new products. I would also like the ability to add new staff bio/photos when we add employees. The site must be able to be edited by myself once we take ownership.
Updates

sorry for the delay. I just uploaded the company logo

Reason: I forced to travel for business. please make any last minute submissions using the logo i uploaded. i will choose on october 25th

Industry/Entity Type

Shopping

```html
<!DOCTYPE html>
<html lang="en">
<head>
<meta charset="utf-8">
<title>Trevol — Brightwave</title>
<link href="https://fonts.googleapis.com/css2?family=Open+Sans:ital,wght@0,400;0,600;0,700;1,400;1,600&family=Raleway:wght@300;400;600&display=swap" rel="stylesheet">
<style>
:root{
  --blue:#3a9ee0;
  --blue-dark:#2b7fc0;
  --ink:#1d1d1f;
  --text:#3b3b3b;
  --muted:#8a8a8a;
  --line:#e3e3e3;
  --panel:#f1f1f1;
  --footer:#141414;
  --footer-bar:#0c0c0c;
  --field:#3a3a3a;
  --red:#c0282d;
  --white:#ffffff;
}
*{box-sizing:border-box;margin:0;padding:0}
html,body{width:1200px;height:2585px;overflow:hidden}
body{position:relative;background:var(--white);font-family:"Open Sans",Arial,sans-serif;color:var(--text)}
.abs{position:absolute}

/* top bar */
.topbar{left:0;top:0;width:1200px;height:43px;border-bottom:1px solid var(--line)}
.topbar .tagline{left:163px;top:14px;font-size:11px;letter-spacing:.4px;color:var(--text)}
.topbar .support{left:760px;top:14px;font-size:11px;color:var(--text);display:flex;align-items:center;gap:6px}
.topbar .signin{left:917px;top:9px;width:72px;height:25px;border:1px solid #ccc;font-size:10px;font-weight:700;letter-spacing:.8px;display:flex;align-items:center;justify-content:center}
.topbar .cart{left:996px;top:9px;width:36px;height:25px;background:var(--blue);display:flex;align-items:center;justify-content:center}

/* nav */
.nav{left:0;top:43px;width:1200px;height:65px;border-bottom:1px solid var(--line)}
.brand{left:168px;top:20px;display:flex;align-items:center;gap:8px;font-family:"Raleway",Arial,sans-serif;font-weight:600;font-size:22px;letter-spacing:1px;color:#5b6a7a}
.brand .dot{width:16px;height:16px;border-radius:50%;background:var(--blue)}
.menu{left:402px;top:28px;display:flex;gap:22px;font-size:11px;color:var(--text)}
.menu .active{color:var(--blue)}
.social{left:962px;top:27px;display:flex;gap:7px}
.social span{width:14px;height:14px;background:#333;border-radius:2px}

/* hero */
.hero{left:0;top:108px;width:1200px;height:305px;background:linear-gradient(90deg,#d9dde2 0%,#9a9ea4 35%,#4a4d52 60%,#2d2f33 100%)}
.hero-visual{left:0;top:0;width:640px;height:305px;background:linear-gradient(135deg,#f1f3f6 0%,#c9ced6 45%,rgba(120,125,135,0) 100%)}
.hero-copy{left:670px;top:76px;color:var(--white);text-align:center;width:380px}
.hero-copy h1{font-family:"Raleway",Arial,sans-serif;font-weight:300;font-size:46px;letter-spacing:1px;line-height:1}
.hero-copy .kicker{margin-top:14px;color:var(--blue);font-size:13px;letter-spacing:1px}
.hero-copy p{margin-top:10px;font-size:14px;letter-spacing:.4px;line-height:1.35}

/* intro */
.intro-title{left:163px;top:456px;font-size:26px;font-weight:700;color:var(--ink);letter-spacing:.2px}
.intro-text{left:163px;top:505px;width:470px;font-size:12.5px;line-height:2;color:var(--text)}
.features{left:168px;top:648px}
.features h3{font-size:22px;font-weight:700;color:var(--ink)}
.features ul{list-style:none;margin-top:4px;font-size:16px;line-height:1.6;color:var(--ink)}
.brushes{left:648px;top:490px;width:410px;height:230px;background:linear-gradient(180deg,#ffffff 0%,#e8ecf3 55%,#c9d3e6 100%)}
.curve1{left:750px;top:730px}
.kit{left:130px;top:816px;width:520px;height:276px;background:linear-gradient(160deg,#ffffff 0%,#dfe6ee 45%,#6f94c6 100%)}
.curve2{left:360px;top:1020px}

.register{left:653px;top:885px}
.register h2{font-size:34px;font-weight:600;color:var(--blue);line-height:1.1}
.register .sub{font-size:26px;font-style:italic;color:var(--blue);line-height:1.2}
.register ul{list-style:none;margin-top:12px;font-size:15px;line-height:1.9;color:var(--ink)}
.register li{display:flex;align-items:center;gap:10px}
.register .cta{margin-top:14px;font-size:12px;font-weight:700;color:var(--red)}

.goal{left:0;top:1178px;width:1200px;text-align:center;font-size:26px;font-style:italic;color:var(--blue);line-height:1.4}

/* about */
.about{left:163px;top:1290px}
.about h2{font-family:"Raleway",Arial,sans-serif;font-weight:400;font-size:30px;color:var(--ink);letter-spacing:.5px}
.about .lead{margin-top:10px;font-size:16px;color:var(--ink);letter-spacing:.3px}
.about .small{margin-top:6px;font-size:12px;color:var(--text)}

.band{left:0;top:1406px;width:1200px;height:250px;background:linear-gradient(90deg,#3a3d42 0%,#6f747b 45%,#4b4f55 70%,#2e3034 100%)}
.card{top:34px;width:152px;height:182px;background:var(--white);padding:8px}
.card .ph{width:136px;height:120px}
.card .lbl{margin-top:8px;font-size:9.5px;color:var(--text);letter-spacing:.3px}
.card .name{font-size:13px;color:var(--ink);letter-spacing:.3px}

/* simple steps */
.simple{left:163px;top:1690px}
.simple h2{font-family:"Raleway",Arial,sans-serif;font-weight:400;font-size:30px;line-height:1.2;color:var(--ink)}
.simple h2 b{font-weight:600}
.simple p{margin-top:10px;font-size:12.5px;color:var(--text)}
.steps{left:163px;top:1817px;width:874px;height:264px;background:var(--panel);overflow:hidden}
.steps ol{position:absolute;left:30px;top:0;width:400px;height:264px;list-style:none;font-size:12.5px;font-weight:700;color:var(--ink);line-height:18px}
.steps li{position:absolute;left:0;white-space:nowrap}
.steps li.on{color:var(--blue)}
.steps li .desc{font-weight:400;font-size:11px;color:var(--blue);margin-top:4px;margin-left:22px;line-height:17px;width:330px;white-space:normal}
.steps .figure{left:450px;top:20px;width:400px;height:228px;background:linear-gradient(140deg,#ffffff 0%,#dfe9f2 45%,#9dc6de 100%)}

/* footer */
.footer{left:0;top:2126px;width:1200px;height:370px;background:var(--footer);color:var(--white)}
.f-brand{left:245px;top:76px;display:flex;align-items:center;gap:8px;font-family:"Raleway",Arial,sans-serif;font-size:22px;letter-spacing:1px}
.f-brand .dot{width:14px;height:14px;border-radius:50%;background:var(--white)}
.f-about{left:258px;top:125px;width:330px;font-size:11px;line-height:1.9}
.f-contact{left:258px;top:222px;font-size:10.5px;line-height:2.5}
.f-contact div{display:flex;align-items:center;gap:10px}
.field{background:var(--field);color:#bdbdbd;font-size:10px;padding:8px 6px}
.btn{font-size:12px;display:flex;align-items:center;justify-content:center}
.btn.reset{background:#bdbdbd;color:#333}
.btn.submit{background:var(--blue);color:var(--white)}
.copyright{left:0;top:2496px;width:1200px;height:89px;background:var(--footer-bar);color:var(--white);font-size:11px;text-align:center;padding-top:38px}
</style>
</head>
<body>

<header class="abs topbar">
  <div class="abs tagline">ENHANCE YOUR PERFORMANCE...AND YOUR PATIENT'S COMFORT</div>
  <div class="abs support">
    <svg width="8" height="12" viewBox="0 0 8 12"><rect x="0.5" y="0.5" width="7" height="11" rx="1.5" fill="none" stroke="#555"/><circle cx="4" cy="9.5" r=".8" fill="#555"/></svg>
    Support: 555-010-4471
  </div>
  <div class="abs signin">SIGN IN</div>
  <div class="abs cart">
    <svg width="18" height="14" viewBox="0 0 18 14"><path d="M1 1h3l2 8h9l2-6H5" fill="none" stroke="#fff" stroke-width="1.6"/><circle cx="7" cy="12" r="1.3" fill="#fff"/><circle cx="14" cy="12" r="1.3" fill="#fff"/></svg>
  </div>
</header>

<nav class="abs nav">
  <div class="abs brand"><span class="dot"></span>TREVOL</div>
  <div class="abs menu">
    <span class="active">Home</span><span>About</span><span>Product</span><span>Electric Toothbrushes</span><span>Dental Health Topics</span><span>Contact Us</span>
  </div>
  <div class="abs social"><span></span><span></span><span></span></div>
</nav>

<section class="abs hero">
  <div class="abs hero-visual" role="img" aria-label="Brightwave prophy handpiece with a blue brush head"></div>
  <div class="abs hero-copy">
    <h1>BRIGHTWAVE</h1>
    <div class="kicker">HEALTHCARE REVOLUTIONIZED</div>
    <p>CHOOSE BRIGHTWAVE™ AIR FOR YOUR<br>HYGIENE CASES</p>
  </div>
</section>

<h2 class="abs intro-title">LOVE BRIGHTWAVE OR NEED MORE BRUSH</h2>
<p class="abs intro-text">The Brightwave™ Air prophylaxis motor is perfect for disposable prophy angles. The powerful handpiece operates at a maximum speed of 2,600 rpm and the patient's stress level will be greatly reduced with the Brightwave™ Air's virtually silent operation.</p>
<div class="abs features">
  <h3>Features:</h3>
  <ul><li>• Accepts all standard prophy angles</li><li>• Quick disconnect nosecone</li><li>• 360-degree swivel</li></ul>
</div>
<div class="abs brushes" role="img" aria-label="Row of disposable prophy angles in white and blue"></div>
<svg class="abs curve1" width="170" height="85" viewBox="0 0 170 85"><path d="M5 15 C 40 70, 110 70, 160 40" fill="none" stroke="#333" stroke-width="1.3" stroke-dasharray="4 4"/><path d="M150 34 L162 39 L154 48" fill="none" stroke="#333" stroke-width="1.3"/></svg>

<div class="abs kit" role="img" aria-label="Brightwave handpiece with toothbrush kit and care products"></div>
<svg class="abs curve2" width="290" height="90" viewBox="0 0 290 90"><path d="M5 60 C 80 95, 200 90, 270 20" fill="none" stroke="#333" stroke-width="1.3" stroke-dasharray="4 4"/><path d="M258 22 L272 16 L272 31" fill="none" stroke="#333" stroke-width="1.3"/></svg>

<div class="abs register">
  <h2>Register your product</h2>
  <div class="sub">and get great benefits</div>
  <ul>
    <li><svg width="18" height="18" viewBox="0 0 18 18"><circle cx="9" cy="9" r="8" fill="none" stroke="#222" stroke-width="1.3"/><path d="M5 9.5l3 3 5-6" fill="none" stroke="#222" stroke-width="1.5"/></svg>Gain access to the latest savings</li>
    <li><svg width="18" height="18" viewBox="0 0 18 18"><circle cx="9" cy="9" r="8" fill="none" stroke="#222" stroke-width="1.3"/><path d="M5 9.5l3 3 5-6" fill="none" stroke="#222" stroke-width="1.5"/></svg>Promotions</li>
    <li><svg width="18" height="18" viewBox="0 0 18 18"><circle cx="9" cy="9" r="8" fill="none" stroke="#222" stroke-width="1.3"/><path d="M5 9.5l3 3 5-6" fill="none" stroke="#222" stroke-width="1.5"/></svg>Product news &amp; more</li>
  </ul>
  <div class="cta">REGISTER NOW</div>
</div>

<p class="abs goal">Our goal is to make sure you leave with a smile<br>on your face!</p>

<section class="abs about">
  <h2>ABOUT OUR PRODUCT</h2>
  <div class="lead">NOTHING COMPARES TO OUR UNIQUE BRIGHTWAVE TECHNOLOGY.</div>
  <div class="small">After 20 years, we're still the #1 recommended sonic power toothbrush brand by dental professionals worldwide.</div>
</section>

<section class="abs band" role="img" aria-label="Dental clinic treatment room in soft focus">
  <div class="abs card" style="left:250px"><div class="ph" style="background:linear-gradient(180deg,#f4f6f8,#b9d7ea)" role="img" aria-label="Electric toothbrushes"></div><div class="lbl">BRIGHTWAVE</div><div class="name">TOOTHBRUSHES</div></div>
  <div class="abs card" style="left:432px"><div class="ph" style="background:linear-gradient(180deg,#f4f6f8,#cfe4c9)" role="img" aria-label="Brush heads"></div><div class="lbl">BRIGHTWAVE</div><div class="name">BRUSH HEADS</div></div>
  <div class="abs card" style="left:619px"><div class="ph" style="background:linear-gradient(180deg,#f4f6f8,#aab9d6)" role="img" aria-label="Airfloss handpiece"></div><div class="lbl">BRIGHTWAVE</div><div class="name">AIRFLOSS</div></div>
  <div class="abs card" style="left:800px"><div class="ph" style="background:linear-gradient(180deg,#e9c1b3,#f3e6e0)" role="img" aria-label="Bright white smile"></div><div class="lbl">BRIGHTWAVE</div><div class="name">WHITENING</div></div>
</section>

<section class="abs simple">
  <h2>IT'S SIMPLE. <b>LET BRIGHTWAVE<br>DO THE WORK FOR YOU.</b></h2>
  <p>Brightwave's unique brush head design means that all you have to do is guide the brush along your teeth – let it do the work.</p>
</section>

<section class="abs steps">
  <ol>
    <li class="on" style="top:28px">1. Choose your brush head.<div class="desc">Your dental professional can help you determine which brush head is right for your oral health needs.</div></li>
    <li style="top:128px">2. Keep the MicroFlow filaments working</li>
    <li style="top:159px">3. Rotaflex will feel different!</li>
    <li style="top:190px">4. Use "M" and "W" motions</li>
    <li style="top:221px">5. The extras</li>
  </ol>
  <div class="abs figure" role="img" aria-label="Prophy handpiece cleaning a tooth model"></div>
</section>

<footer class="abs footer">
  <div class="abs f-brand"><span class="dot"></span>TREVOL</div>
  <p class="abs f-about">The Brightwave™ Air prophylaxis motor is perfect for disposable prophy angles. The powerful handpiece operates at a maximum speed of 2,600 rpm</p>
  <div class="abs f-contact">
    <div><svg width="10" height="12" viewBox="0 0 10 12"><path d="M5 0.5C2.5 0.5 1 2.3 1 4.4 1 7.5 5 11.5 5 11.5S9 7.5 9 4.4C9 2.3 7.5.5 5 .5z" fill="#fff"/></svg>Brightwave™</div>
    <div><svg width="10" height="12" viewBox="0 0 10 12"><path d="M2 .5l2 3-1.2 1.2c.6 1.6 1.8 2.8 3.3 3.4L7.3 7l2.2 2.4-1.5 2C4 11 .5 6 .5 1.8z" fill="#fff"/></svg>0800-555-0142 &nbsp;|&nbsp; 0977-555-0199</div>
    <div><svg width="12" height="9" viewBox="0 0 12 9"><rect x=".5" y=".5" width="11" height="8" fill="#fff"/><path d="M.5 .5l5.5 4.5L11.5.5" fill="none" stroke="#141414"/></svg>hello@trevol.com</div>
  </div>
  <div class="abs field" style="left:620px;top:85px;width:165px;height:30px">your name</div>
  <div class="abs field" style="left:798px;top:85px;width:165px;height:30px">your email</div>
  <div class="abs field" style="left:620px;top:127px;width:343px;height:30px">your subject</div>
  <div class="abs" style="left:930px;top:132px;width:26px;height:20px;background:#9a9a9a"></div>
  <div class="abs field" style="left:620px;top:170px;width:343px;height:112px">your message</div>
  <div class="abs btn reset" style="left:695px;top:298px;width:125px;height:40px">Reset</div>
  <div class="abs btn submit" style="left:835px;top:298px;width:128px;height:40px">Submit</div>
</footer>
<div class="abs copyright">Copyright 2014 @Trevol, All right reserved.</div>

</body>
</html>
```